Business Card Design

An energy company designed around renewable energy and energy storage that focuses on providing its energy at points on the grid that reduce costs and add value to the system.

Industry/Entity Type

Business

Contact Information for Business Card

Martin Delacroix
Executive Vice President
41 K ST NE
Washington, DC 20017
240-555-0183
mdelacroix@harborvoltco.example

```html
<!DOCTYPE html>
<html lang="en">
<head>
<meta charset="utf-8">
<title>Harbor Volt — Business Card</title>
<link href="https://fonts.googleapis.com/css2?family=Nunito+Sans:wght@400;700;900&display=swap" rel="stylesheet">
<style>
  :root {
    --stage: #e6e6e6;
    --card: #f1f1f1;
    --card-shade: #dcdcdc;
    --ink: #141414;
    --ink-soft: #2a2a2a;
  }
  html, body {
    margin: 0;
    width: 1200px;
    height: 900px;
    overflow: hidden;
    background: var(--stage);
    font-family: "Nunito Sans", "Helvetica Neue", Arial, sans-serif;
  }
  .card {
    position: absolute;
    left: 100px;
    top: 164px;
    width: 1000px;
    height: 572px;
    background: var(--card);
    box-shadow: 0 18px 40px rgba(0,0,0,0.12);
    overflow: hidden;
    color: var(--ink);
  }
  .card__texture {
    position: absolute;
    inset: 0;
    background:
      radial-gradient(ellipse at 80% 10%, rgba(0,0,0,0.07), transparent 55%),
      linear-gradient(180deg, transparent 55%, var(--card-shade) 100%);
  }
  .wordmark {
    position: absolute;
    left: 52px;
    top: 40px;
    margin: 0;
    font-weight: 900;
    font-size: 84px;
    letter-spacing: -1px;
    line-height: 1;
    color: var(--ink);
  }
  .person {
    position: absolute;
    left: 58px;
    top: 262px;
  }
  .person__name {
    margin: 0;
    font-weight: 700;
    font-size: 31px;
    color: var(--ink);
  }
  .person__title {
    margin: 6px 0 0;
    font-weight: 400;
    font-size: 26px;
    color: var(--ink-soft);
  }
  .contacts {
    position: absolute;
    left: 500px;
    top: 208px;
    margin: 0;
    padding: 0;
    list-style: none;
    font-size: 25px;
    color: var(--ink-soft);
  }
  .contacts__item {
    display: flex;
    align-items: center;
    gap: 14px;
    height: 42px;
  }
  .contacts__item--indent { padding-left: 22px; }
  .contacts__icon { width: 26px; height: 26px; flex: none; }
</style>
</head>
<body>
  <article class="card">
    <div class="card__texture" role="img" aria-label="Distressed speckled grain texture across the card"></div>

    <h1 class="wordmark">HARBOR VOLT</h1>

    <div class="person">
      <p class="person__name">Martin Delacroix</p>
      <p class="person__title">Executive Vice President</p>
    </div>

    <ul class="contacts">
      <li class="contacts__item">
        <svg class="contacts__icon" viewBox="0 0 24 24" aria-hidden="true">
          <circle cx="12" cy="12" r="10.5" fill="none" stroke="#141414" stroke-width="2"/>
          <path d="M8.5 7c.6-.6 1.3-.4 1.6.1l1 1.6c.3.5.2 1-.2 1.4l-.6.5c.5 1.2 1.4 2.1 2.6 2.6l.5-.6c.4-.4.9-.5 1.4-.2l1.6 1c.5.3.7 1 .1 1.6-1 1-2.3 1.2-3.6.5-2.3-1.2-3.9-2.8-5-5-.6-1.3-.5-2.6.6-3.5z" fill="#141414"/>
        </svg>
        <span>20017 240-555-0183</span>
      </li>
      <li class="contacts__item">
        <svg class="contacts__icon" viewBox="0 0 24 24" aria-hidden="true">
          <circle cx="12" cy="12" r="10.5" fill="none" stroke="#141414" stroke-width="2"/>
          <rect x="6.5" y="8" width="11" height="8" rx="1" fill="none" stroke="#141414" stroke-width="1.6"/>
          <path d="M6.8 8.5 12 12.6l5.2-4.1" fill="none" stroke="#141414" stroke-width="1.6"/>
        </svg>
        <span>mdelacroix@harborvoltco.example</span>
      </li>
      <li class="contacts__item contacts__item--indent">
        <svg class="contacts__icon" viewBox="0 0 24 24" aria-hidden="true">
          <path d="M12 2a7 7 0 0 0-7 7c0 5 7 13 7 13s7-8 7-13a7 7 0 0 0-7-7zm0 9.5A2.5 2.5 0 1 1 12 6.5a2.5 2.5 0 0 1 0 5z" fill="#141414"/>
        </svg>
        <span>41 K ST NE Washington, DC</span>
      </li>
    </ul>
  </article>
</body>
</html>
```